Criação de Papelaria (6 itens) para Roupas, Jóias & acessórios
" Vendemos artigos de vestuário infantil apenas de forma online. Temos nosso site e veiculamos o nosso conteúdo pelo facebook e instagram "

```html
<!DOCTYPE html>
<html lang="pt-BR">
<head>
<meta charset="UTF-8">
<title>Pipo Lili – Cartão de Visita</title>
<link href="https://fonts.googleapis.com/css2?family=Nunito:wght@400;600;800&display=swap" rel="stylesheet">
<style>
  :root {
    --page: #e6e9ee;
    --navy: #1c2234;
    --white: #ffffff;
    --ink: #3a3f4d;
    --green: #7cb82f;
    --pink: #e8307e;
    --blue: #27a9e1;
    --yellow: #f6c21c;
    --orange: #f58220;
    --purple: #8e4fb5;
    --grey: #7d8390;
  }
  * { box-sizing: border-box; margin: 0; padding: 0; }
  html, body { width: 1200px; height: 1200px; overflow: hidden; }
  body {
    background: var(--page);
    font-family: "Nunito", sans-serif;
    display: flex;
    flex-direction: column;
    align-items: center;
    justify-content: center;
    gap: 60px;
  }
  .card {
    position: relative;
    width: 880px;
    height: 503px;
    border-radius: 22px;
    overflow: hidden;
    box-shadow: 0 14px 30px rgba(28, 34, 52, 0.18);
  }
  .confetti-band {
    position: absolute;
    left: 40px;
    right: 40px;
    height: 14px;
    border-radius: 7px;
    background: linear-gradient(90deg, var(--pink), var(--orange), var(--yellow), var(--green), var(--blue), var(--purple), var(--pink));
    opacity: 0.9;
  }

  /* Front */
  .card--front { background: var(--white); color: var(--ink); }
  .card--front .confetti-band.top { top: 34px; }
  .card--front .confetti-band.middle { top: 240px; }
  .card--front .confetti-band.bottom { bottom: 34px; }
  .contact-list {
    position: absolute;
    top: 84px;
    left: 60px;
    list-style: none;
    display: flex;
    flex-direction: column;
    gap: 16px;
    font-size: 22px;
    font-weight: 600;
  }
  .contact-list li { display: flex; align-items: center; gap: 14px; }
  .contact-icon {
    width: 30px; height: 30px; border-radius: 50%;
    background: var(--green);
    display: flex; align-items: center; justify-content: center;
    flex: none;
  }
  .contact-icon svg { width: 18px; height: 18px; }
  .person {
    position: absolute;
    top: 280px;
    right: 60px;
    text-align: right;
  }
  .person-name { font-size: 34px; font-weight: 800; color: var(--green); letter-spacing: 1px; }
  .person-role { font-size: 20px; font-weight: 600; color: var(--grey); margin-top: 2px; }
  .brand {
    display: flex;
    flex-direction: column;
    align-items: center;
  }
  .brand-row { display: flex; align-items: center; gap: 12px; }
  .brand-dot { width: 22px; height: 22px; border-radius: 50%; background: var(--pink); }
  .brand-name { font-weight: 800; color: var(--pink); line-height: 1; }
  .brand-tag { font-weight: 600; letter-spacing: 2px; }
  .card--front .brand { position: absolute; right: 60px; bottom: 70px; }
  .card--front .brand-name { font-size: 46px; }
  .card--front .brand-tag { font-size: 18px; color: var(--ink); }

  /* Back */
  .card--back { background: var(--navy); color: var(--white); }
  .card--back .confetti-band.top { top: 40px; }
  .card--back .confetti-band.bottom { bottom: 110px; }
  .card--back .brand {
    position: absolute;
    left: 0; right: 0; top: 150px;
  }
  .card--back .brand-name { font-size: 84px; }
  .card--back .brand-dot { width: 36px; height: 36px; }
  .card--back .brand-tag { font-size: 28px; color: var(--white); margin-top: 6px; }
  .website {
    position: absolute;
    left: 0; right: 0; bottom: 52px;
    text-align: center;
    font-size: 26px;
    font-weight: 600;
    letter-spacing: 1px;
  }
</style>
</head>
<body>
  <section class="card card--front">
    <div class="confetti-band top" role="img" aria-label="Faixa de confetes coloridos"></div>
    <ul class="contact-list">
      <li>
        <span class="contact-icon">
          <svg viewBox="0 0 24 24"><path fill="#fff" d="M6.6 10.8a15 15 0 0 0 6.6 6.6l2.2-2.2c.3-.3.7-.4 1-.2 1.1.4 2.3.6 3.6.6.6 0 1 .4 1 1V20c0 .6-.4 1-1 1A17 17 0 0 1 3 4c0-.6.4-1 1-1h3.5c.6 0 1 .4 1 1 0 1.3.2 2.5.6 3.6.1.3 0 .7-.2 1z"/></svg>
        </span>
        (11) 90000-1234
      </li>
      <li>
        <span class="contact-icon">
          <svg viewBox="0 0 24 24"><path fill="none" stroke="#fff" stroke-width="2" d="M3 6h18v12H3z M3 6l9 7 9-7"/></svg>
        </span>
        contato@pipolili.com
      </li>
      <li>
        <span class="contact-icon"></span>
        /PipoLili.ModaInfantil
      </li>
    </ul>
    <div class="confetti-band middle" role="img" aria-label="Faixa de confetes coloridos"></div>
    <div class="person">
      <p class="person-name">Nome Completo</p>
      <p class="person-role">Cargo | Função</p>
    </div>
    <div class="brand">
      <div class="brand-row">
        <span class="brand-dot"></span>
        <span class="brand-name">Pipo Lili</span>
      </div>
      <span class="brand-tag">moda infantil</span>
    </div>
    <div class="confetti-band bottom" role="img" aria-label="Faixa de confetes coloridos"></div>
  </section>

  <section class="card card--back">
    <div class="confetti-band top" role="img" aria-label="Faixa de confetes coloridos"></div>
    <div class="brand">
      <div class="brand-row">
        <span class="brand-dot"></span>
        <span class="brand-name">Pipo Lili</span>
      </div>
      <span class="brand-tag">moda infantil</span>
    </div>
    <div class="confetti-band bottom" role="img" aria-label="Faixa de confetes coloridos"></div>
    <p class="website">www.pipolilimodainfantil.com.br</p>
  </section>
</body>
</html>
```